Wholistic Health Clinic (Chiropractic Osteopathic Naturapathic Homeopathic New Website Design

Create a beautiful website for Fenwick Chiropractic clinic that has been in the Sutherland Shire for over 40 years, that exemplifies the passion for helping people with their health goals using that may include a variety of techniques including Chiropractic, Osteopathy, Acupuncture, Applied Kinesiology, Retained Neonatal Reflexes, Nutritional Advice, Exercise Prescription, Decompression therapy, Massage and Stress management techniques.
We have a wholistic approach that includes Nutritional, Emotional and Physical health

(A more detailed draft will be supplied shortly)

Pages:
Home page
About Us Page
Team Page
Contact page
Terms of service Page
Privacy Page
and any other relevant page(s)

Will supply photos for:
- The Team Page and their qualifications & brief resume
- About Us page

Will supply logos for:
BPN
TORVEX
PLORIVEN
GRANTLEAF
MVA
KPO

Target Market(s)

main target Parents of young children and those 20's to 60's who live in the Sutherland Shire & have disposable income (that said almost everybody would benefit from their services)

Coding

Coded - Design and coding required

Number of Pages Required

5+ page

Font styles to use
Sans Serif

Requirements
Must have
• Please follow the brief

1. Easy to manage ourselves to add alerts (like Covid 19 compliance & Harbel week etc.) & update content like photos of team members etc.
2. Must be responsive and look good on mobile devices
3. must be fast loading
4. Logo on every page
5. Easy navigation on every page
6. Phone number must be clickable
7. Terms of service & Privacy pages
8. Slider on page 1 using photo of healthy people of all ages enjoying various lifestyles & ability to add other photos easily
Should not have
• no testimonials or any non compliant elements according to the BPN

```html
<!DOCTYPE html>
<html lang="en">
<head>
<meta charset="utf-8">
<title>Fenwick Chiropractic</title>
<link href="https://fonts.googleapis.com/css2?family=Poppins:wght@300;400;500;600;700&display=swap" rel="stylesheet">
<style>
:root{
  --green:#23962a;
  --green-soft:#c8e6c3;
  --ink:#111111;
  --text:#2c2c2c;
  --brown:#3a2e22;
  --navy:#0b418c;
  --sky:#7093c2;
  --white:#ffffff;
  --grey-light:#d4d4d4;
  --grey-mid:#a9a9a9;
}
*{margin:0;padding:0;box-sizing:border-box}
html,body{width:1200px;height:3971px;overflow:hidden;background:var(--white)}
body{position:relative;font-family:'Poppins',sans-serif;color:var(--text)}
.abs{position:absolute}
.logo{font-weight:700;font-size:20px;color:var(--ink);letter-spacing:.2px}
.nav a{position:absolute;top:39px;font-size:15px;color:#333;text-decoration:none}
.btn{position:absolute;display:flex;align-items:center;justify-content:center;background:var(--green);color:var(--white);font-weight:600;border-radius:2px;text-decoration:none}
.login{left:981px;top:30px;width:94px;height:38px;font-size:13px;gap:8px}
.hero-title{left:123px;top:166px;font-size:39px;font-weight:600;line-height:46px;color:var(--ink)}
.hero-text{left:123px;top:286px;width:380px;font-size:15.5px;line-height:24px;color:#333}
.know{left:123px;top:407px;width:156px;height:46px;font-size:14px}
.video{left:298px;top:418px;display:flex;align-items:center;gap:10px;font-size:14.5px;font-weight:500;color:var(--green);text-decoration:underline}
.photo{position:absolute}
.photo-grey{background:linear-gradient(160deg,var(--grey-light) 0%,var(--grey-mid) 100%);border-radius:40px}
.section-title{left:0;width:1200px;text-align:center;font-size:33px;font-weight:600;line-height:46px;color:var(--ink)}
.service{position:absolute;top:768px;width:260px;text-align:center}
.service .icon{width:42px;height:42px;border-radius:10px;margin:0 auto;display:flex;align-items:center;justify-content:center;box-shadow:0 4px 10px rgba(0,0,0,.15)}
.service .icon span{width:7px;height:10px;border:1.5px solid var(--white)}
.service h3{margin-top:38px;font-size:19.5px;font-weight:500;color:var(--ink)}
.service p{margin:14px auto 0;width:190px;font-size:13.5px;line-height:23px;color:#333}
.know-more{left:532px;top:971px;width:160px;height:47px;font-size:14px}
.adv-title{font-size:32px;font-weight:600;color:var(--brown)}
.adv-text{font-size:14px;line-height:23px;color:var(--brown)}
.check{position:absolute;left:663px;display:flex;align-items:center;gap:26px;font-size:14.5px;color:#333}
.check svg{flex:none}
.bubble{position:absolute;background:var(--white);border-radius:24px;box-shadow:0 4px 14px rgba(0,0,0,.07);display:flex;align-items:center;justify-content:center;font-size:14px;color:#333}
.avatar{position:absolute;border-radius:50%;border:3px solid var(--white)}
.hero-need{left:0;top:2584px;width:1200px;text-align:center;font-size:31px;font-weight:600;color:var(--ink)}
.need-text{left:350px;top:2648px;width:500px;text-align:center;font-size:14px;line-height:23px;color:var(--ink)}
.experts{left:494px;top:2731px;width:185px;height:45px;font-size:14.5px}
.parallax{left:0;top:3177px;width:1200px;height:470px;background:linear-gradient(180deg,#6b8ec4 0%,#7598c6 60%,#6c8dbb 100%)}
.stat{position:absolute;top:3448px;width:207px;color:var(--white)}
.stat .bar{height:3px;background:rgba(255,255,255,.3)}
.stat .bar i{display:block;height:3px;background:var(--white)}
.stat b{display:block;margin-top:24px;font-size:22px;font-weight:300}
.stat small{display:block;font-size:10px}
.footer{left:0;top:3698px;width:1200px;height:273px;background:var(--navy);color:var(--white)}
.footer h4{position:absolute;font-size:17px;font-weight:600}
.footer a{position:absolute;font-size:14px;color:var(--white);text-decoration:none}
</style>
</head>
<body>

<header>
  <div class="abs logo" style="left:123px;top:35px">YOUR LOGO</div>
  <nav class="nav">
    <a style="left:320px">Home</a>
    <a style="left:392px">About Us</a>
    <a style="left:488px">Our Team</a>
    <a style="left:584px">Contact US</a>
    <a style="left:680px">Terms of service</a>
    <a style="left:824px">Privacy</a>
  </nav>
  <a class="btn login">
    <svg width="18" height="16" viewBox="0 0 18 16" fill="none" stroke="#fff" stroke-width="1.6"><path d="M7 3V1.5h9.5v13H7V13"/><path d="M1 8h9M7 5l3 3-3 3"/></svg>
    LOGIN
  </a>
</header>

<section class="hero">
  <h1 class="abs hero-title">We are a Fenwick<br>Chiropractic clinic</h1>
  <p class="abs hero-text">Tools, tutorials, design and innovation experts, all in one place! The most intuitive way to imagine your next user experience.</p>
  <a class="btn know">Know More</a>
  <a class="abs video"><svg width="14" height="16" viewBox="0 0 14 16"><path d="M0 0l14 8-14 8z" fill="#23962a"/></svg>Watch the Video</a>
  <div class="photo" role="img" aria-label="Woman in a blue shirt holding her sore neck" style="left:595px;top:116px;width:469px;height:390px;background:linear-gradient(160deg,#f3f5fa 0%,#c9d6f0 40%,#7f9fe0 80%,#eef2fb 100%)"></div>
</section>

<section class="services">
  <svg class="abs" style="left:0;top:740px" width="1200" height="356" viewBox="0 0 1200 356" aria-hidden="true">
    <defs><linearGradient id="g1" x1="0" y1="0" x2="0" y2="1"><stop offset="0" stop-color="#fff"/><stop offset="1" stop-color="#c8e6c3"/></linearGradient></defs>
    <path d="M0 0H1200V262Q600 470 0 262Z" fill="url(#g1)"/>
  </svg>
  <h2 class="abs section-title" style="top:628px">We exemplify the passion for helping<br>people with their health goals</h2>
  <div class="service" style="left:109px"><div class="icon" style="background:#7a4fc2"><span></span></div><h3>Chiropractic</h3><p>While most people enjoy casino gambling,</p></div>
  <div class="service" style="left:356px"><div class="icon" style="background:#f5b400"><span></span></div><h3>Applied Kinesiology</h3><p>Sports betting, lottery and bingo playing for the fun</p></div>
  <div class="service" style="left:612px"><div class="icon" style="background:#ef3b3b"><span></span></div><h3>Decompression therapy</h3><p>The Pagevine page defines the individual.</p></div>
  <div class="service" style="left:841px"><div class="icon" style="background:#3fa3f0"><span></span></div><h3>Physical health</h3><p>Personal choices and the overall personality of the person.</p></div>
  <a class="btn know-more">KNOW MORE</a>
</section>

<section class="advantage">
  <h2 class="abs adv-title" style="left:124px;top:1324px">Write a Advantage</h2>
  <p class="abs adv-text" style="left:124px;top:1388px;width:430px">Vestibulum purus quam, scelerisque ut, mollis sed, nonummy id, metus. Praesent porttitor, nulla vitae posuere iaculis, arcu nisl dignissim dolor, a pretium mi sem ut ipsum.</p>
  <p class="abs adv-text" style="left:124px;top:1482px;font-weight:600;font-size:13.5px">Accessory makers</p>
  <p class="abs adv-text" style="left:124px;top:1514px;width:420px">While most people enjoy casino gambling, sports betting, lottery and bingo playing for the fun</p>
  <div class="photo photo-grey" role="img" aria-label="Photo of a patient's back during a treatment consultation" style="left:705px;top:1254px;width:364px;height:385px"></div>

  <div class="photo photo-grey" role="img" aria-label="Photo of a patient's neck and shoulders during a treatment consultation" style="left:123px;top:1789px;width:333px;height:387px"></div>
  <h2 class="abs adv-title" style="left:663px;top:1812px;color:var(--ink)">Write a Advantage</h2>
  <p class="abs adv-text" style="left:663px;top:1876px;width:420px;color:#333">Vestibulum purus quam, scelerisque ut, mollis sed, nonummy id, metus. Praesent porttitor, nulla vitae posuere iaculis, arcu nisl dignissim dolor, a pretium mi sem ut ipsum.</p>
  <div class="check" style="top:1979px"><svg width="30" height="30" viewBox="0 0 30 30"><circle cx="15" cy="15" r="13.5" fill="#d9f0d6" stroke="#23962a" stroke-width="2"/><circle cx="15" cy="15" r="9.5" fill="#23962a"/><path d="M10.5 15.2l3 3 6-6.2" fill="none" stroke="#fff" stroke-width="1.8"/></svg>Vestibulum purus quam</div>
  <div class="check" style="top:2049px"><svg width="30" height="30" viewBox="0 0 30 30"><circle cx="15" cy="15" r="13.5" fill="#d9f0d6" stroke="#23962a" stroke-width="2"/><circle cx="15" cy="15" r="9.5" fill="#23962a"/><path d="M10.5 15.2l3 3 6-6.2" fill="none" stroke="#fff" stroke-width="1.8"/></svg>Vestibulum purus quam</div>
  <div class="check" style="top:2119px"><svg width="30" height="30" viewBox="0 0 30 30"><circle cx="15" cy="15" r="13.5" fill="#d9f0d6" stroke="#23962a" stroke-width="2"/><circle cx="15" cy="15" r="9.5" fill="#23962a"/><path d="M10.5 15.2l3 3 6-6.2" fill="none" stroke="#fff" stroke-width="1.8"/></svg>Vestibulum purus quam</div>
</section>

<section class="experts-section">
  <svg class="abs" style="left:0;top:2387px" width="1200" height="800" viewBox="0 0 1200 800" aria-hidden="true">
    <defs><linearGradient id="g2" x1="0" y1="0" x2="0" y2="1"><stop offset="0" stop-color="#c8e6c3"/><stop offset=".75" stop-color="#fff"/></linearGradient></defs>
    <path d="M0 110Q600 -110 1200 110V800H0Z" fill="url(#g2)"/>
  </svg>
  <div class="bubble" style="left:142px;top:2541px;width:234px;height:44px">Donec sodales sagittis</div>
  <div class="avatar" role="img" aria-label="Portrait of a smiling woman" style="left:95px;top:2578px;width:84px;height:84px;background:#c98f78"></div>
  <div class="bubble" style="left:702px;top:2486px;width:239px;height:44px">Donec sodales sagittis magna.</div>
  <div class="avatar" role="img" aria-label="Portrait of a young man" style="left:910px;top:2520px;width:85px;height:85px;background:#5a3a30"></div>
  <h2 class="abs hero-need">Need a super hero?</h2>
  <p class="abs need-text">Nullam accumsan lorem in dui. Suspendisse pulvinar, augue ac venenatis condimentum, sem libero volutpat nibh scelerisque ut, mollis sed, nonummy id, metus.</p>
  <a class="btn experts">View our experts</a>
  <div class="bubble" style="left:113px;top:2785px;width:228px;height:40px">Donec sodales sagittis magna.</div>
  <div class="avatar" role="img" aria-label="Portrait of a man in a white shirt" style="left:291px;top:2819px;width:83px;height:83px;background:#d9c2b4"></div>
  <div class="bubble" style="left:813px;top:2765px;width:212px;height:40px">Donec sodales sagittis magna.</div>
  <div class="avatar" role="img" aria-label="Portrait of a person with a camera" style="left:990px;top:2797px;width:85px;height:85px;background:#3d4b5a"></div>
  <div class="bubble" style="left:452px;top:2868px;width:274px;height:44px">Donec sodales sagittis</div>
  <div class="avatar" role="img" aria-label="Portrait of a smiling blonde woman" style="left:678px;top:2902px;width:84px;height:84px;background:#2f3a52"></div>
</section>

<section class="abs parallax" role="img" aria-label="Woman in black stretching her arms against a blue sky">
</section>
<div class="abs" style="left:0;top:3315px;width:1200px;text-align:center;font-size:14px;color:#fff">MENU CLIPPING</div>
<div class="abs" style="left:0;top:3362px;width:1200px;text-align:center;font-size:31px;font-weight:300;color:#fff">Celebrate Motion paralax scroll.</div>
<div class="stat" style="left:262px"><div class="bar"><i style="width:76%"></i></div><b>200%</b><small>Smoother</small></div>
<div class="stat" style="left:495px"><div class="bar"><i style="width:75%"></i></div><b>200%</b><small>Lighter</small></div>
<div class="stat" style="left:729px"><div class="bar"><i style="width:87%"></i></div><b>200ma</b><small>Micro Awesomeness</small></div>

<footer class="abs footer">
  <div class="abs logo" style="left:123px;top:81px;color:#fff">YOUR LOGO</div>
  <h4 style="left:401px;top:76px">Quick Links</h4>
  <a style="left:401px;top:121px">About Us</a>
  <a style="left:401px;top:151px">Our</a>
  <a style="left:401px;top:181px">Team</a>
  <a style="left:401px;top:211px">Contact</a>
  <h4 style="left:614px;top:76px">Legal</h4>
  <a style="left:614px;top:121px">Disclaimer</a>
  <a style="left:614px;top:151px">Privacy Policy</a>
  <a style="left:614px;top:181px">Terms of Service</a>
  <h4 style="left:823px;top:76px;width:225px;text-align:center">POLITICS</h4>
  <p class="abs" style="left:823px;top:116px;width:240px;font-size:14px;font-weight:500;line-height:23px">While most people enjoy casino gambling, sports betting, lottery</p>
</footer>

</body>
</html>
```